Manuka honey wholesales and export company needs a website

We are a Manuka honey Wholesale and export company based in New Zealand and needing a website to attract new clients.
We produce one of the worlds best honeys so we need a clean, modern look that lets everybody know that we can supply our product around the world.
We source only the finest Manuka honey from some of the most remote parts of New Zealand and send it around the world for everyone to enjoy.
We need a website that will allow people to inquire about export or bulk purchasing as well as a buying tab with pricing but one that we can add photos to as our product labels are not complete yet.
We also support and supply local farmers markets and a page dedicated to this would be good with details on when and where they are.

Here are links to other manuka honey websites to get an idea
http://www.petalgrove.example.nz/
http://www.dalvoren.example.nz/key-ingredients/manuka-honey/nz200417?gclid=Tq8WLPmZrsXDNQBYehFK27JtRBOzZvWqKx3HTRnYV5Pd83UkMqWfjLeS64-jqVXNcEAbsGLy0nTpbYcQoFxZ4M7YLRC

Target Market(s)

The general public, retail shops and exporters

Industry/Entity Type

Health And Wellness

Number of Pages Required

5+ page

Font styles to use
Serif

Requirements
Must have
• 1. A page and contact details for Export and wholesale inquiries
• Tobias Frennick
• Export manager
• +64 21 830 419
• tbfrennick@mailvista.example.nz
• 2. Page for the farmers market we supply our product to.
• Details....
• Contact: Owen Pascoe
• +64 21 648 1073
• kettlebloomnz@postbay.example.com
• MARKET INFORMATION
• Harbourlight Market
• The market operates year round and is located on Fenwick Square.*
• http://harbourlight.example.org/le-pavot-market/
• Saturday 8am-1pm
• Sunday 9am-1pm
• Ashgrove Village Market
• http://www.ashgrovefarmersmarket.example.nz/
• 42 Larchmont Rd, Ashgrove, Auckland 2591, New Zealand
• Market is held each Sunday from 8:30am-1pm.
• 3. An information page on manuka honey....i will attach info but most of the info you can find on other manuka honey websites..
• Health benefits..
• There are two main components of Manuka honey which give it many health benefits:
• - Hydrogen peroxide, a naturally antibiotic found in Manuka honey.
• - Methylglyoxal (MG). A powerful antibiotic compound found in large quantities in Manuka honey.
• What is MGO?
• The MGO indicates the amount of Methylglyoxal in the honey. The higher the MGO rating the more antibacterial properties are in the honey.
• Proven health Benefits of Active Manuka are....
• Aiding in the treatment of:
• - -Common Cold and Flu
• - -sore throats
• - -cuts and abrasions
• - -Reduce hair loss and scalp problems
• - -treating fungal infections
• - -Burns
• - -ulsers
• - -strengthening the immune system
• 4. A product page with a range of our products with a link yo by direct from us
• The details for this page will need to be added later as we are still doing our range!
Nice to have
• Feel free to make up a mission statement or whatever inspires you to make this a great website.
Should not have
• Go crazy please! I trust you will come up with something amazing :)

```html
<!DOCTYPE html>
<html lang="en">
<head>
<meta charset="utf-8">
<title>Kettlebloom Honey NZ Limited</title>
<link rel="stylesheet" href="https://fonts.googleapis.com/css2?family=Merriweather:ital,wght@0,700;0,900;1,900&family=Open+Sans:wght@400;600;700&family=Quicksand:wght@500;600&display=swap">
<style>
:root{
  --honey:#f1cb0c;
  --gold:#e6b726;
  --amber:#d79a1c;
  --ink:#2b2b2b;
  --night:#333333;
  --coal:#222222;
  --text:#555555;
  --muted:#9a9a9a;
  --paper:#ffffff;
  --mist:#f1f1f1;
}
*{box-sizing:border-box;margin:0;padding:0}
html,body{width:1200px;height:3191px;overflow:hidden}
body{position:relative;background:var(--paper);font-family:"Open Sans",Arial,sans-serif;color:var(--text)}
.abs{position:absolute}
.serif{font-family:"Merriweather",Georgia,serif}

/* header */
.site-header{position:absolute;left:0;top:0;width:1200px;height:143px;background:var(--ink)}
.brand{left:85px;top:56px;display:flex;align-items:center;gap:10px;color:#fff;font-size:21px;font-weight:400}
.brand-mark{width:14px;height:14px;border-radius:50%;background:var(--honey)}
.util{top:9px;right:175px;font-size:10px;color:#bbb;letter-spacing:.3px;display:flex;align-items:center;gap:8px}
.util .icon{width:12px;height:12px}
.phone{top:8px;right:75px;font-size:11px;color:#ccc;display:flex;align-items:center;gap:6px}
.cart{left:979px;top:49px;width:142px;height:36px;border:1px solid #555;border-radius:18px;color:#bbb;font-size:10px;display:flex;align-items:center;justify-content:center;gap:8px}
.main-nav{left:0;top:100px;width:1200px;height:43px;background:#262626;border-top:1px solid #3a3a3a}
.main-nav a{position:absolute;top:0;height:43px;line-height:43px;font-size:11px;font-weight:600;color:#ddd;text-decoration:none;letter-spacing:.4px}
.main-nav a.active{background:var(--honey);color:var(--ink);padding:0 26px;left:74px}
.search{left:1092px;top:112px;width:18px;height:18px}

/* hero */
.hero{left:0;top:143px;width:1200px;height:680px;background:radial-gradient(ellipse at 28% 55%,#c9861d 0%,#8a4d12 35%,#4a2b16 70%,#3a2a1f 100%)}
.hero-photo{width:100%;height:100%;background:linear-gradient(90deg,rgba(0,0,0,0) 45%,rgba(220,180,90,.45) 70%,rgba(120,95,60,.3) 100%)}
.hero-title{left:0;top:405px;width:1200px;text-align:center;font-size:66px;font-style:italic;font-weight:900;color:#fff}
.hero-title .accent{color:var(--honey)}
.hero-sub{left:0;top:508px;width:1200px;text-align:center;font-size:19px;font-weight:700;color:var(--honey);letter-spacing:.3px}
.btn{position:absolute;display:flex;align-items:center;justify-content:center;font-size:11px;font-weight:700;letter-spacing:.3px;text-decoration:none}
.btn-pill{height:36px;border-radius:18px}
.btn-yellow{background:var(--honey);color:var(--ink)}
.btn-ghost{border:2px solid #fff;color:#fff}
.slide-arrow{top:453px;width:74px;height:70px;background:rgba(255,255,255,.15)}

/* overview */
.overview{left:0;top:823px;width:1200px;height:545px;background:var(--mist)}
.bees{left:700px;top:0;width:500px;height:545px;background:linear-gradient(90deg,rgba(241,241,241,1),rgba(205,205,205,.8))}
.overview-photo{left:38px;top:71px;width:419px;height:446px;background:radial-gradient(circle at 40% 55%,#f0a21c 0%,#d98410 35%,#8a4a1a 65%,rgba(241,241,241,0) 72%)}
.section-title{font-size:31px;font-weight:900;color:var(--gold);letter-spacing:.5px}
.section-sub{font-size:11px;font-weight:700;color:var(--ink);letter-spacing:.3px}
.dots{display:flex;align-items:center;gap:4px}
.dots i{display:block;width:9px;height:9px;border-radius:50%;background:#555}
.dots b{display:block;height:1px;width:70px;background:#bbb}
.copy{font-size:13px;line-height:23px;color:var(--text)}
.btn-box{height:38px;font-size:11px}

/* manuka */
.manuka{left:0;top:1368px;width:1200px;height:543px;background:var(--gold)}
.manuka-frame{left:85px;top:53px;width:1028px;height:430px;background:#fff;padding:11px}
.manuka-panel{width:100%;height:100%;background:linear-gradient(90deg,#3b1d10 0%,#2a130b 40%,#1a0c0a 100%);position:relative}
.manuka-photo{left:40px;top:40px;width:520px;height:350px;background:radial-gradient(ellipse at 50% 55%,#e3961f 0%,#a8561a 40%,rgba(42,19,11,0) 72%)}

/* products */
.products-title{left:0;top:1980px;width:1200px;text-align:center}
.product{position:absolute;width:196px}
.product-photo{width:196px;height:164px;border:2px solid #e6e6e6;background:radial-gradient(circle at 50% 60%,#f2a92a 0%,#e0c27a 35%,#fbf7ef 70%)}
.price{position:absolute;right:8px;top:0;width:36px;height:34px;background:var(--gold);clip-path:polygon(0 0,100% 0,100% 75%,50% 100%,0 75%);color:#fff;font-size:13px;font-weight:700;text-align:center;line-height:28px}
.product-name{font-family:"Quicksand",Arial,sans-serif;font-weight:600;font-size:20px;color:var(--ink);margin-top:10px;line-height:22px}
.product-desc{font-size:10px;color:var(--muted);line-height:13px;margin-top:2px}

/* contact */
.contact{left:0;top:2734px;width:1200px;height:398px;background:var(--night)}
.contact .section-title{color:var(--honey)}
.contact .section-sub{color:#fff}
.c-text{font-size:12px;color:#ccc;line-height:18px}
.c-role{font-size:9px;color:#aaa;letter-spacing:.3px}
.divider{left:547px;top:20px;width:1px;height:360px;background:#4a4a4a}
.badge{left:513px;top:150px;width:68px;height:68px;border-radius:50%;background:var(--honey)}
.field{position:absolute;border-bottom:1px solid #555;font-size:11px;color:#bbb;padding-bottom:10px}
.submit{background:var(--honey);color:var(--ink)}

/* footer */
.site-footer{left:0;top:3132px;width:1200px;height:59px;background:var(--coal)}
.social{position:absolute;top:15px;width:30px;height:30px;border-radius:50%;background:var(--honey)}
</style>
</head>
<body>

<header class="site-header">
  <div class="abs brand"><span class="brand-mark"></span>Kettlebloom Honey NZ Limited</div>
  <div class="abs util">
    <svg class="icon" viewBox="0 0 12 12"><circle cx="6" cy="4" r="2.6" fill="#f1cb0c"/><path d="M1 12c0-3 2.3-5 5-5s5 2 5 5z" fill="#f1cb0c"/></svg>
    MY ACCOUNT &nbsp;|&nbsp; SIGNUP
  </div>
  <div class="abs phone">
    <svg width="14" height="14" viewBox="0 0 14 14"><circle cx="7" cy="7" r="6" fill="none" stroke="#f1cb0c" stroke-width="1.4"/><path d="M5 4l1.2 1.6-.8.9c.4.9 1.1 1.6 2 2l.9-.8L10 9l-1 1.2C6.6 10 4 7.4 3.9 5z" fill="#f1cb0c"/></svg>
    (012) 234 5678
  </div>
  <div class="abs cart">
    <svg width="14" height="12" viewBox="0 0 14 12"><path d="M0 1h2.5l2 7h7l1.5-5H4" fill="none" stroke="#bbb" stroke-width="1.3"/><circle cx="5.5" cy="10.5" r="1.1" fill="#bbb"/><circle cx="10.5" cy="10.5" r="1.1" fill="#bbb"/></svg>
    YOUR CART (0)
  </div>
  <nav class="abs main-nav">
    <a class="active" href="#">HOME</a>
    <a style="left:200px" href="#">ABOUT US</a>
    <a style="left:317px" href="#">PROCESS</a>
    <a style="left:428px" href="#">ABOUT MANUKA</a>
    <a style="left:585px" href="#">SHOP</a>
    <a style="left:670px" href="#">OFFERS</a>
    <a style="left:766px" href="#">CONTACT</a>
  </nav>
  <svg class="abs search" viewBox="0 0 18 18"><circle cx="7" cy="7" r="5.5" fill="none" stroke="#ddd" stroke-width="2"/><path d="M11 11l5.5 5.5" stroke="#ddd" stroke-width="2.2"/></svg>
</header>

<section class="abs hero">
  <div class="hero-photo" role="img" aria-label="Jar of golden manuka honey with a wooden dipper beside honeycomb on a rustic table"></div>
  <svg class="abs slide-arrow" style="left:0;top:310px" viewBox="0 0 74 70"><path d="M44 18L28 35l16 17" fill="none" stroke="#fff" stroke-width="2"/></svg>
  <svg class="abs slide-arrow" style="left:1126px;top:310px" viewBox="0 0 74 70"><path d="M30 18l16 17-16 17" fill="none" stroke="#fff" stroke-width="2"/></svg>
</section>
<h1 class="abs serif hero-title">Straight From The <span class="accent">Hive</span></h1>
<p class="abs hero-sub">DISCOVER THE NATURAL WONDERS OF MANUKA HONEY</p>
<a class="btn btn-pill btn-yellow" style="left:472px;top:631px;width:122px" href="#">SHOP NOW</a>
<a class="btn btn-pill btn-ghost" style="left:598px;top:631px;width:123px" href="#">SHOP NOW</a>

<section class="abs overview">
  <div class="abs bees" role="img" aria-label="Faint background photo of honey bees on comb"></div>
  <div class="abs overview-photo" role="img" aria-label="Honey pot with dipper dripping honey next to honeycomb pieces"></div>
  <h2 class="abs serif section-title" style="left:543px;top:76px">OVERVIEW</h2>
  <div class="abs dots" style="left:543px;top:127px"><i></i><i></i></div>
  <p class="abs section-sub" style="left:519px;top:145px">AN INTRODUCTION ABOUT COMPANY</p>
  <p class="abs copy" style="left:521px;top:210px;width:570px">Lorem Ipsum is simply dummy text of the printing and typesetting industry. Lorem Ipsum has been the industry's standard dummy text ever since the 1500s, when an unknown printer took a galley of type and scrambled it to make a type specimen book. It has survived not only five centuries, but also the leap into electronic typesetting, remaining essentially unchanged. It was popularised in the 1960s with the release of Letraset sheets containing Lorem Ipsum passages, and more recently with desktop publishing software like Aldus PageMaker including versions of Lorem Ipsum.</p>
  <a class="btn btn-box btn-yellow" style="left:521px;top:405px;width:137px" href="#">KNOW MORE</a>
</section>

<section class="abs manuka">
  <div class="abs manuka-frame">
    <div class="manuka-panel">
      <div class="abs manuka-photo" role="img" aria-label="Glass jars of manuka honey with a honey dipper on a dark table"></div>
      <h2 class="abs serif section-title" style="left:0;width:1006px;text-align:center;top:38px;color:var(--honey)">MANUKA HONEY</h2>
      <div class="abs dots" style="left:481px;top:86px"><i></i><i></i></div>
      <p class="abs section-sub" style="left:0;width:1006px;text-align:center;top:104px;color:#fff">AN INTRODUCTION ABOUT COMPANY</p>
      <p class="abs copy" style="left:544px;top:136px;width:415px;color:#ccc;font-size:12.5px;line-height:27px">It is a long established fact that a reader will be distracted by the readable content of a page when looking at its layout. The point of using Lorem Ipsum is that it has a more-or-less normal distribution of letters, as opposed to using 'Content here, content here', making it look like readable English. Many desktop publishing packages and web page editors now use Lorem Ipsum as their default model text.</p>
      <a class="btn" style="left:544px;top:321px;width:101px;height:36px;border:2px solid var(--honey);color:var(--honey)" href="#">KNOW MORE</a>
    </div>
  </div>
</section>

<div class="products-title abs">
  <h2 class="serif section-title">OUR PRODUCTS</h2>
  <div class="dots" style="justify-content:center;margin-top:10px"><b></b><i></i><i></i><b></b></div>
  <p class="section-sub" style="margin-top:8px">ONLINE SHOPPING OF OUR PRODUCTS</p>
</div>

<div class="product" style="left:177px;top:2115px"><div class="product-photo" role="img" aria-label="Two jars of honey"></div><span class="price">$7</span><h3 class="product-name">Duis autemve</h3><p class="product-desc">Nam liber tempor cum soluta nobis</p></div>
<div class="product" style="left:392px;top:2115px"><div class="product-photo" role="img" aria-label="Honey pot wrapped in cloth with dipper"></div><span class="price">$5</span><h3 class="product-name">Lorem ipsum do</h3><p class="product-desc">Tempor cum soluta nobis is</p></div>
<div class="product" style="left:606px;top:2115px"><div class="product-photo" role="img" aria-label="Jar of honey with wooden dipper"></div><span class="price">$17</span><h3 class="product-name">Claritas est etia</h3><p class="product-desc">Hiber tempor cum soluta nobis is</p></div>
<div class="product" style="left:820px;top:2115px"><div class="product-photo" role="img" aria-label="Honey jar with cloth cover"></div><span class="price">$6</span><h3 class="product-name">Investigationes dem</h3><p class="product-desc">Nam liber tempor cum soluta nobis</p></div>

<div class="product" style="left:177px;top:2392px"><div class="product-photo" role="img" aria-label="Bowl of honey with honeycomb and ginger"></div><span class="price">$9</span><h3 class="product-name">Fitterarum formas</h3><p class="product-desc">Xam is tempor cum soluta nobis is</p></div>
<div class="product" style="left:392px;top:2392px"><div class="product-photo" role="img" aria-label="Glass jar of light honey"></div><span class="price">$15</span><h3 class="product-name">Fegentis in</h3><p class="product-desc">Ror cum soluta nobis is eleifend</p></div>
<div class="product" style="left:606px;top:2392px"><div class="product-photo" role="img" aria-label="Honey jar beside honeycomb"></div><span class="price">$16</span><h3 class="product-name">Decima et quinta</h3><p class="product-desc">Empor cum soluta nobis is eleifend</p></div>
<div class="product" style="left:820px;top:2392px"><div class="product-photo" role="img" aria-label="Two tall jars of dark honey"></div><span class="price">$3</span><h3 class="product-name">Rigation quin</h3><p class="product-desc">Nam liber tempor cum soluta nobis</p></div>

<a class="btn btn-box btn-yellow" style="left:517px;top:2652px;width:166px" href="#">VIEW ALL PRODUCTS</a>

<section class="abs contact">
  <h2 class="abs serif section-title" style="left:100px;top:42px">CONTACT INFO</h2>
  <div class="abs dots" style="left:116px;top:86px"><b></b><i></i><i></i><b></b></div>
  <p class="abs section-sub" style="left:116px;top:102px">AN INTRODUCTION ABOUT COMPANY</p>

  <svg class="abs" style="left:111px;top:158px" width="16" height="20" viewBox="0 0 16 20"><path d="M8 0a7 7 0 0 0-7 7c0 5 7 13 7 13s7-8 7-13a7 7 0 0 0-7-7z" fill="var(--honey)"/><circle cx="8" cy="7" r="2.6" fill="#333"/></svg>
  <p class="abs c-text" style="left:166px;top:153px;width:230px">42 Larchmont Rd, Ashgrove,<br>Auckland 2591, New Zealand</p>

  <p class="abs c-text" style="left:166px;top:217px;font-size:13px">TOBIAS FRENNICK</p>
  <p class="abs c-role" style="left:166px;top:240px">EXPORT MANAGER</p>
  <p class="abs c-text" style="left:336px;top:217px;font-size:13px">OWEN PASCOE</p>
  <p class="abs c-role" style="left:336px;top:240px">MARKET INFORMATION</p>

  <svg class="abs" style="left:109px;top:272px" width="20" height="20" viewBox="0 0 20 20"><circle cx="10" cy="10" r="9" fill="none" stroke="var(--honey)" stroke-width="1.6"/><path d="M7 5l1.8 2.4-1.2 1.3c.6 1.3 1.6 2.3 2.9 2.9l1.3-1.2L14.2 12l-1.4 1.8C9.4 13.6 6 10.2 5.8 6.8z" fill="var(--honey)"/></svg>
  <p class="abs c-text" style="left:166px;top:272px">+64 21 830 419</p>
  <p class="abs c-text" style="left:336px;top:272px">+64 21 648 1073</p>

  <svg class="abs" style="left:108px;top:318px" width="22" height="16" viewBox="0 0 22 16"><rect width="22" height="16" fill="var(--honey)"/><path d="M1 1l10 8 10-8" fill="none" stroke="#333" stroke-width="1.6"/></svg>
  <p class="abs c-text" style="left:166px;top:316px;font-size:10.5px">tbfrennick@mailvista.example.nz</p>
  <p class="abs c-text" style="left:336px;top:316px;font-size:10.5px">kettlebloomnz@postbay.example.com</p>

  <div class="abs divider"></div>
  <div class="abs badge"></div>
  <svg class="abs" style="left:535px;top:170px" width="24" height="28" viewBox="0 0 24 28"><rect x="2" y="2" width="17" height="23" fill="none" stroke="#333" stroke-width="2"/><path d="M6 9h9M6 14h9M6 19h6" stroke="#333" stroke-width="2"/><path d="M15 22l7-9 2 2-7 9-3 1z" fill="#333"/></svg>

  <p class="abs c-text" style="left:604px;top:58px;width:520px;font-size:11.5px">Please fill this form to details and information about Exports and Whole Sale Inquiries.<br>&nbsp;Our &nbsp;team &nbsp;will revert you very soon.</p>
  <div class="field" style="left:626px;top:128px;width:476px">Name</div>
  <div class="field" style="left:626px;top:196px;width:222px">Phone</div>
  <div class="field" style="left:868px;top:196px;width:234px">Email</div>
  <div class="field" style="left:626px;top:290px;width:476px">Your Inquiry</div>
  <a class="btn submit" style="left:626px;top:335px;width:476px;height:38px" href="#">SUBMIT NOW</a>
</section>

<footer class="abs site-footer">
  <p class="abs" style="left:100px;top:21px;font-size:11px;color:#777">© 2017 | Privacy policy</p>
  <span class="social" style="left:973px" aria-label="Social link"></span>
  <span class="social" style="left:1008px" aria-label="Social link"></span>
  <span class="social" style="left:1044px" aria-label="Social link"></span>
  <span class="social" style="left:1080px" aria-label="Social link"></span>
</footer>

</body>
</html>
```